Xmas Greeting for Email for Corvath Solutions

We would love to have a beautifully designed Xmas card that we can send to our clients .
The card will be used to thank our clients for their support during the year and to wish them a Merry Xmas and a Good New year (2020).

We would like a design that is simple and very elegant.

Target Market(s)

Our clients

Font styles to use
Script

Colors

Designer to choose colors to be used in the design.

Requirements
Must have
• 1. Our logo (see attached)
• 2. A message that thanks our clients for their support during the year.
• 3. the message "Merry Christmas & Happy New Year"
• 4. Design must be simple and elegant

```html
<!DOCTYPE html>
<html lang="en">
<head>
<meta charset="utf-8">
<title>Corvath Solutions – Season's Greetings</title>
<link rel="stylesheet" href="https://fonts.googleapis.com/css2?family=Kaushan+Script&family=Montserrat:wght@400&display=swap">
<style>
  :root {
    --page: #ffffff;
    --card-edge: #e2e2e2;
    --ink: #626262;
    --silver-dark: #8a8684;
    --silver-mid: #c9c7c6;
    --silver-light: #f2f2f2;
    --mark: #d6d6d6;
  }
  html, body {
    margin: 0;
    padding: 0;
    width: 1200px;
    height: 1138px;
    overflow: hidden;
    background: var(--page);
  }
  .canvas {
    position: relative;
    width: 1200px;
    height: 1138px;
  }
  .card {
    position: absolute;
    left: 244px;
    top: 74px;
    width: 708px;
    height: 1012px;
    box-sizing: border-box;
    border: 2px solid var(--card-edge);
    background: var(--page);
    overflow: hidden;
  }
  .card__art {
    position: absolute;
    inset: 0;
  }
  .greeting {
    position: absolute;
    inset: 0;
    margin: 0;
    font-family: "Kaushan Script", cursive;
    font-weight: 400;
    color: var(--ink);
  }
  .greeting span {
    position: absolute;
    white-space: nowrap;
    line-height: 1;
  }
  .greeting .lg { font-size: 58px; }
  .greeting .sm { font-size: 33px; }
  .signoff__dot {
    position: absolute;
    left: 318px;
    top: 874px;
    width: 54px;
    height: 54px;
    border-radius: 50%;
    background: var(--mark);
  }
  .signoff__name {
    position: absolute;
    left: 392px;
    top: 896px;
    margin: 0;
    font-family: "Montserrat", sans-serif;
    font-weight: 400;
    font-size: 21px;
    line-height: 1;
    letter-spacing: 2px;
    color: var(--ink);
    text-transform: uppercase;
    white-space: nowrap;
  }
  .thanks {
    position: absolute;
    left: 392px;
    top: 936px;
    width: 290px;
    margin: 0;
    font-family: "Montserrat", sans-serif;
    font-weight: 400;
    font-size: 12px;
    line-height: 1.45;
    color: var(--ink);
  }
</style>
</head>
<body>
<main class="canvas">
  <section class="card">
    <svg class="card__art" viewBox="0 0 708 1012" width="708" height="1012" role="img" aria-label="Silver winter illustration of large and small snowflakes with sparkling bokeh lights, fading to white at the lower right">
      <defs>
        <linearGradient id="silverTone" x1="0" y1="0" x2="1" y2="1">
          <stop offset="0" stop-color="var(--silver-mid)"/>
          <stop offset="0.3" stop-color="var(--silver-dark)"/>
          <stop offset="0.55" stop-color="var(--silver-mid)"/>
          <stop offset="0.8" stop-color="var(--silver-light)"/>
          <stop offset="1" stop-color="var(--silver-light)"/>
        </linearGradient>
        <radialGradient id="whiteGlow" cx="0.82" cy="0.72" r="0.55">
          <stop offset="0" stop-color="#ffffff" stop-opacity="1"/>
          <stop offset="0.6" stop-color="#ffffff" stop-opacity="0.9"/>
          <stop offset="1" stop-color="#ffffff" stop-opacity="0"/>
        </radialGradient>
      </defs>
      <rect width="708" height="1012" fill="url(#silverTone)"/>
      <rect width="708" height="1012" fill="url(#whiteGlow)"/>
    </svg>

    <h1 class="greeting" aria-label="Merry Christmas and a Happy New Year from all at Corvath Solutions">
      <span class="lg" style="left:385px; top:585px;">Merry</span>
      <span class="lg" style="left:448px; top:636px;">Christmas</span>
      <span class="sm" style="left:497px; top:690px;">and a</span>
      <span class="lg" style="left:398px; top:702px;">Happy</span>
      <span class="lg" style="left:410px; top:755px;">New</span>
      <span class="lg" style="left:512px; top:780px;">Year</span>
      <span class="sm" style="left:388px; top:836px;">from all</span>
      <span class="sm" style="left:460px; top:858px;">at</span>
    </h1>

    <div class="signoff__dot"></div>
    <p class="signoff__name">Corvath Solutions</p>
    <p class="thanks">Thank you for your support throughout the year – wishing you a joyful 2020.</p>
  </section>
</main>
</body>
</html>
```